TR Advisory Business Cards - High End AV / Low Voltage Company

We are low voltage AV company that specializes in high end clients on the residential side and larger businesses on the commercial side. We want something modern, tech looking but also something that is extremely professional looking. We have uploaded our logos and postcards we already have in the field. Along with a picture of one of our wrapped vans. Our website is at www.trvadvisory.example and our primary colors are the orange, green, grey and blue all military color finishes.

We are interesting in the slogans "Pairing You with the Right Technology" or "Leading the Lowcountry in Tech"

Target Market(s)

We focus on 70% Commercial and 30% Residential Customers

Industry/Entity Type

Low Voltage, AV Company

Contact Information for Business Card

Name - Dorian Fairweather, Title - Owner, Office Phone - 555-714-3096, Mobile Phone - 555-802-4173, E-Mail - d@trvadvisory.example, Website: www.trvadvisory.example

Font styles to use
Sans Serif

Requirements
Must have
• Must have Name, Title, Work Phone & Mobile, Website and Logo.
Nice to have
• We want something that will impress our higher end clients with a great logo
Should not have
• Too traditional or plain.

```html
<!DOCTYPE html>
<html lang="en">
<head>
<meta charset="utf-8">
<title>TR Advisory Business Card</title>
<link rel="stylesheet" href="https://fonts.googleapis.com/css2?family=Montserrat:wght@500;600;700&family=Inter:wght@400;500&display=swap">
<style>
  :root {
    --orange: #ec6a3c;
    --ink: #141414;
    --grey-text: #6f6f6f;
    --grey-soft: #e4e4e4;
    --grey-fade: #f4f4f4;
    --divider: #bdbdbd;
    --card: #ffffff;
    --backdrop: #ececec;
  }
  * { margin: 0; padding: 0; box-sizing: border-box; }
  html, body { width: 1200px; height: 800px; overflow: hidden; }
  body { background: var(--backdrop); position: relative; font-family: "Inter", Arial, sans-serif; }

  .business-card {
    position: absolute; left: 142px; top: 125px;
    width: 915px; height: 550px;
    background: var(--card); overflow: hidden;
  }

  .footer-field {
    position: absolute; left: 50px; right: 50px; bottom: 0; height: 115px;
    border-radius: 50% 50% 0 0 / 100% 100% 0 0;
    background: linear-gradient(to bottom, var(--grey-soft), var(--grey-fade));
  }

  .tagline {
    position: absolute; left: 0; right: 0; top: 392px;
    text-align: center;
    font-family: "Montserrat", Arial, sans-serif; font-weight: 600;
    font-size: 20px; letter-spacing: 4.2px; color: var(--grey-text);
  }

  .brand {
    position: absolute; left: 60px; top: 170px; width: 340px;
    display: flex; align-items: center; justify-content: center; gap: 14px;
  }
  .brand-dot { width: 26px; height: 26px; border-radius: 50%; background: var(--orange); flex: none; }
  .brand-name {
    font-family: "Montserrat", Arial, sans-serif; font-weight: 700;
    font-size: 40px; color: var(--orange); letter-spacing: 1px; white-space: nowrap;
  }

  .divider { position: absolute; left: 455px; top: 102px; width: 1px; height: 212px; background: var(--divider); }

  .contact { position: absolute; left: 505px; top: 114px; }
  .contact-name {
    font-family: "Montserrat", Arial, sans-serif; font-weight: 700;
    font-size: 25px; color: var(--orange); letter-spacing: 0.6px; line-height: 1;
  }
  .contact-title { font-size: 17px; color: var(--ink); margin-top: 6px; line-height: 1.1; }
  .contact-list { list-style: none; margin-top: 32px; }
  .contact-list li {
    display: flex; align-items: center; gap: 9px;
    font-size: 20px; color: var(--ink); height: 29px; margin-left: 5px;
  }
  .contact-list li.gap-before { margin-top: 10px; }
  .contact-list svg { width: 15px; height: 15px; flex: none; stroke: var(--orange); fill: none; stroke-width: 1.8; }
</style>
</head>
<body>
  <main class="business-card">
    <div class="footer-field" role="img" aria-label="Soft grey decorative band along the bottom edge"></div>

    <p class="tagline">LEADING THE LOWCOUNTRY IN TECH</p>

    <div class="brand">
      <span class="brand-dot"></span>
      <span class="brand-name">TR Advisory</span>
    </div>

    <div class="divider"></div>

    <section class="contact">
      <h1 class="contact-name">DORIAN FAIRWEATHER</h1>
      <p class="contact-title">Owner</p>
      <ul class="contact-list">
        <li><svg viewBox="0 0 16 16"><path d="M4 1.5l2.5 3-1.5 2c1 2 2.5 3.5 4.5 4.5l2-1.5 3 2.5-1.5 2.5C7.5 16 0 8.5 1.5 3z"/></svg>555-714-3096</li>
        <li><svg viewBox="0 0 16 16"><rect x="4" y="1" width="8" height="14" rx="1.5"/><path d="M7 12.5h2"/></svg>555-802-4173</li>
        <li class="gap-before"><svg viewBox="0 0 16 16"><rect x="1.5" y="3.5" width="13" height="9" rx="1"/><path d="M2 4l6 4.5L14 4"/></svg>d@trvadvisory.example</li>
        <li><svg viewBox="0 0 16 16"><circle cx="8" cy="8" r="6.5"/><path d="M1.5 8h13M8 1.5c-3 3.5-3 9.5 0 13M8 1.5c3 3.5 3 9.5 0 13"/></svg>www.trvadvisory.example</li>
      </ul>
    </section>
  </main>
</body>
</html>
```